Birchmead Assurance Group Ltd needs a business card and logo

We need a logo for documents, invoices etc and a business card to match. We are a health auditing, training and consulting company based in NZ and working in both Australia and NZ. We ensure health organisations meet all their compliance requirements and develop expertise in the health auditing sector. The design should in some way reflect either symbols for quality management in the health sector.

Target Market(s)

Health providers and those wishing to increase their capability in meeting and understanding compliance requirements

Industry/Entity Type

Business

Contact Information for Business Card

Logo plus contact details

Logo Text

Health auditing, consultancy and training

Requirements
Must have
• Name and contact details director: Clara Hotham, chotham@bag-example.co.nz, PO Box 419, Kerrowdale, NZ, cell +6427390516

```html
<!DOCTYPE html>
<html lang="en">
<head>
<meta charset="utf-8">
<title>Birchmead Assurance Group – Business Card</title>
<link rel="stylesheet" href="https://fonts.googleapis.com/css2?family=Didact+Gothic&family=Old+Standard+TT:ital@1&display=swap">
<style>
  :root {
    --green: #8cc63f;
    --blue: #27aae1;
    --orange: #f7941d;
    --pink: #ec1f7a;
    --ink: #333333;
    --white: #ffffff;
    --bg-light: #fbfbfb;
    --bg-edge: #e4e4e4;
  }
  * { margin: 0; padding: 0; box-sizing: border-box; }
  html, body { width: 1200px; height: 686px; overflow: hidden; background: var(--bg-edge); }
  .card {
    position: relative;
    width: 1200px;
    height: 686px;
    overflow: hidden;
    background: radial-gradient(ellipse at 45% 45%, var(--bg-light) 0%, #f3f3f3 55%, var(--bg-edge) 100%);
  }

  /* Brand block */
  .brand {
    position: absolute;
    left: 94px;
    top: 98px;
    display: flex;
    align-items: center;
    gap: 22px;
  }
  .brand-dot {
    width: 96px;
    height: 96px;
    border-radius: 50%;
    background: var(--green);
  }
  .brand-name {
    font-family: "Didact Gothic", sans-serif;
    font-size: 36px;
    line-height: 1.15;
    color: var(--ink);
  }

  /* Ribbon banners */
  .ribbons { position: absolute; inset: 0; filter: drop-shadow(0 3px 3px rgba(0,0,0,0.28)); }
  .ribbon {
    position: absolute;
    left: 0;
    background: var(--green);
    color: var(--white);
    display: flex;
    align-items: center;
  }
  .ribbon--name    { top: 285px; height: 72px; width: 547px; clip-path: polygon(0 0, 502px 0, 100% 50%, 502px 100%, 0 100%); }
  .ribbon--phone   { top: 366px; height: 77px; width: 656px; clip-path: polygon(0 0, 606px 0, 100% 50%, 606px 100%, 0 100%); }
  .ribbon--email   { top: 454px; height: 79px; width: 757px; clip-path: polygon(0 0, 704px 0, 100% 50%, 704px 100%, 0 100%); }
  .ribbon--address { top: 546px; height: 78px; width: 842px; clip-path: polygon(0 0, 784px 0, 100% 50%, 784px 100%, 0 100%); }

  .person-name {
    font-family: "Didact Gothic", sans-serif;
    font-variant: small-caps;
    font-size: 56px;
    padding-left: 86px;
    letter-spacing: 0;
    line-height: 1;
    -webkit-text-stroke: 0.8px var(--white);
  }
  .contact-text {
    font-family: "Old Standard TT", serif;
    font-style: italic;
    font-size: 38px;
    letter-spacing: 2px;
    line-height: 1;
  }
  .contact-sep { margin: 0 16px 0 20px; font-size: 30px; }
  .icon { display: block; flex: none; }
  .icon--phone { margin-left: 70px; }
  .icon--mail  { margin-left: 30px; }
  .ribbon--address .contact-text { padding-left: 32px; letter-spacing: 3px; }

  /* Colour strip */
  .colour-strip { position: absolute; left: 0; bottom: 0; width: 1200px; height: 32px; display: flex; }
  .colour-strip span { height: 100%; }
  .strip-green  { width: 294px; background: var(--green); }
  .strip-blue   { width: 306px; background: var(--blue); }
  .strip-orange { width: 301px; background: var(--orange); }
  .strip-pink   { width: 299px; background: var(--pink); }
</style>
</head>
<body>
<main class="card">
  <div class="brand">
    <div class="brand-dot"></div>
    <div class="brand-name">Birchmead<br>Assurance Group</div>
  </div>

  <div class="ribbons">
    <div class="ribbon ribbon--name">
      <span class="person-name">Clara Hotham</span>
    </div>

    <div class="ribbon ribbon--phone">
      <svg class="icon icon--phone" width="37" height="34" viewBox="0 0 37 34" aria-hidden="true">
        <rect x="0" y="0" width="37" height="34" rx="7" fill="#ffffff"/>
        <path d="M11 7c1.5-.6 2.4 0 3 1.3l1.6 3.4c.5 1.1.2 2-.8 2.7l-1.2.9c1 2.6 3 4.7 5.6 5.9l.9-1.2c.7-1 1.6-1.2 2.7-.7l3.3 1.6c1.300.6 1.8 1.6 1.2 3l-.8 1.7c-.6 1.3-2 2-3.5 1.8C15.7 26.4 9.6 20.2 8.5 12c-.2-1.5.5-2.9 1.8-3.5z" fill="var(--green)"/>
      </svg>
      <span class="contact-text"><span class="contact-sep">:</span>+6427390516</span>
    </div>

    <div class="ribbon ribbon--email">
      <svg class="icon icon--mail" width="74" height="40" viewBox="0 0 74 40" aria-hidden="true">
        <rect x="2" y="2" width="70" height="36" rx="3" fill="none" stroke="#ffffff" stroke-width="4"/>
        <path d="M4 4 L37 24 L70 4" fill="none" stroke="#ffffff" stroke-width="4"/>
      </svg>
      <span class="contact-text"><span class="contact-sep">:</span>chotham@bag-example.co.nz</span>
    </div>

    <div class="ribbon ribbon--address">
      <span class="contact-text">PO Box 419, Kerrowdale, NZ,</span>
    </div>
  </div>

  <div class="colour-strip">
    <span class="strip-green"></span>
    <span class="strip-blue"></span>
    <span class="strip-orange"></span>
    <span class="strip-pink"></span>
  </div>
</main>
</body>
</html>
```